Service Plan Sales Flyer

The Watchpost Depot (www.kelvarnguard.com) is a commercial security integrator that installs security cameras, access control, intrusion, two-way radios and perimeter security. We require a one page flyer for our service plan for new and existing customers. The price of the service plan is $299/yr and includes the following;
1. Discounted service rate of $118/hr
2. Free remote support ($85/hr without a plan)
3. Free remote training
4. Priority support

Please review our brochure attached and create a one page sales flyer with the end goal of having the client sign up for our annual service plan . The plan will automatically renew every year. Email sales@kelvarnguard.com.

Target Market(s)

commercial industrial clients - no residential

Industry/Entity Type

review our website at www.kelvarnguard.com

Colors
0054AA
0677BA
7BADD7
CADEEF
E8F1F8
EE7325
F08F49
F5BC92
FAE3D3
FDF4ED

Requirements
Must have
• call to action
Should not have
• too many colors

```html
<!DOCTYPE html>
<html lang="en">
<head>
<meta charset="utf-8">
<title>Service Plan Flyer – The Watchpost Depot</title>
<link rel="stylesheet" href="https://fonts.googleapis.com/css2?family=Bebas+Neue&family=Montserrat:wght@400;500;600;700&family=Oswald:wght@500;600;700&display=swap">
<style>
  :root {
    --navy: #1c2d5a;
    --red: #ea4230;
    --grey-band: #d5d7dc;
    --backdrop: #c8c8c8;
    --white: #ffffff;
    --ink: #1f2230;
    --media-a: #e9ecf1;
    --media-b: #c9ced8;
  }
  * { box-sizing: border-box; margin: 0; padding: 0; }
  html, body { width: 1200px; height: 2387px; overflow: hidden; }
  body { background: var(--backdrop); font-family: "Montserrat", sans-serif; color: var(--ink); position: relative; }

  .flyer { position: absolute; left: 0; top: 346px; width: 1200px; height: 1695px; background: var(--white); overflow: hidden; box-shadow: 0 6px 18px rgba(0,0,0,.25); }

  .brand { position: absolute; top: 66px; left: 0; width: 100%; display: flex; justify-content: center; align-items: center; gap: 22px; }
  .brand-mark { width: 54px; height: 54px; background: var(--red); }
  .brand-name { font-family: "Oswald", sans-serif; font-weight: 700; font-size: 62px; color: var(--navy); text-transform: uppercase; letter-spacing: 1px; white-space: nowrap; }

  .plan-pill { position: absolute; left: 48px; top: 259px; width: 473px; height: 78px; background: var(--red); border-radius: 18px; color: var(--white); font-weight: 700; font-size: 50px; text-align: center; line-height: 78px; letter-spacing: 1px; white-space: nowrap; }
  .plan-price { position: absolute; left: 58px; top: 344px; font-family: "Bebas Neue", sans-serif; font-weight: 400; font-size: 158px; line-height: 1; color: var(--navy); letter-spacing: 0; white-space: nowrap; }

  .product-media { position: absolute; left: 580px; top: 199px; width: 586px; height: 387px; background: radial-gradient(ellipse at 55% 50%, var(--media-a), var(--media-b) 85%, var(--white)); border-radius: 6px; }

  .systems { position: absolute; left: 0; top: 599px; width: 100%; height: 214px; background: var(--grey-band); }
  .systems-divider { position: absolute; left: 600px; top: 40px; width: 2px; height: 140px; background: var(--navy); }
  .system { position: absolute; display: flex; align-items: center; height: 70px; }
  .system-icon { width: 70px; height: 70px; flex: none; }
  .system-arrow { width: 0; height: 0; border-left: 13px solid var(--red); border-top: 8px solid transparent; border-bottom: 8px solid transparent; margin: 0 26px 0 14px; flex: none; }
  .system-label { font-family: "Bebas Neue", sans-serif; font-weight: 400; font-size: 40px; line-height: 1; padding-top: 4px; color: var(--navy); text-transform: uppercase; white-space: nowrap; }

  .benefits { position: absolute; left: 0; top: 819px; width: 100%; height: 751px; background: var(--navy); }
  .card { position: absolute; background: var(--white); border: 3px solid var(--red); border-radius: 22px; padding: 30px 40px 0 32px; }
  .card-title { font-size: 31px; font-weight: 500; color: var(--navy); margin-bottom: 22px; white-space: nowrap; }
  .card-title strong { color: var(--red); font-weight: 700; }
  .card-text { font-size: 22.5px; line-height: 1.2; color: var(--ink); }

  .renew { position: absolute; left: 0; width: 100%; text-align: center; color: var(--white); white-space: nowrap; }
  .renew-title { top: 651px; font-size: 30px; font-weight: 700; }
  .renew-note { top: 705px; font-size: 18.5px; font-weight: 400; }

  .contact { position: absolute; left: 0; top: 1575px; width: 100%; height: 120px; background: var(--red); border-top: 6px solid var(--white); display: flex; align-items: center; justify-content: space-between; padding: 0 30px 6px 36px; }
  .phone { width: 420px; height: 57px; background: var(--white); border-radius: 10px; display: flex; align-items: center; padding-left: 22px; gap: 18px; font-weight: 700; font-size: 38px; color: var(--navy); white-space: nowrap; flex: none; }
  .contact-link { display: flex; align-items: center; gap: 12px; color: var(--white); font-weight: 600; font-size: 19px; white-space: nowrap; }
  .contact-icon { width: 42px; height: 42px; flex: none; }
</style>
</head>
<body>
<main class="flyer">

  <header class="brand">
    <span class="brand-mark"></span>
    <span class="brand-name">The Watchpost Depot</span>
  </header>

  <div class="plan-pill">SERVICE PLAN</div>
  <div class="plan-price">$299/YR</div>

  <div class="product-media" role="img" aria-label="Product photo: office door with access reader, monitoring screen showing a camera view, dome and bullet security cameras"></div>

  <section class="systems">
    <div class="system" style="left:88px; top:35px;">
      <svg class="system-icon" viewBox="0 0 70 70"><circle cx="35" cy="35" r="33" fill="#1c2d5a"/><circle cx="35" cy="35" r="27" fill="none" stroke="#fff" stroke-width="2"/><rect x="24" y="27" width="20" height="11" rx="2" fill="#fff" transform="rotate(15 34 32)"/><rect x="21" y="39" width="3" height="10" fill="#fff"/><rect x="21" y="43" width="9" height="3" fill="#fff"/></svg>
      <span class="system-arrow"></span>
      <span class="system-label">Security Camera System</span>
    </div>
    <div class="system" style="left:88px; top:110px;">
      <svg class="system-icon" viewBox="0 0 70 70"><circle cx="35" cy="35" r="33" fill="#1c2d5a"/><circle cx="35" cy="35" r="27" fill="none" stroke="#fff" stroke-width="2"/><rect x="24" y="21" width="22" height="28" rx="3" fill="none" stroke="#fff" stroke-width="2.5"/><rect x="28" y="25" width="14" height="6" fill="#fff"/><g fill="#fff"><rect x="28" y="34" width="4" height="3"/><rect x="33" y="34" width="4" height="3"/><rect x="38" y="34" width="4" height="3"/><rect x="28" y="40" width="4" height="3"/><rect x="33" y="40" width="4" height="3"/><rect x="38" y="40" width="4" height="3"/></g></svg>
      <span class="system-arrow"></span>
      <span class="system-label">Intrusion Alarm</span>
    </div>
    <div class="systems-divider"></div>
    <div class="system" style="left:655px; top:35px;">
      <svg class="system-icon" viewBox="0 0 70 70"><circle cx="35" cy="35" r="33" fill="#1c2d5a"/><circle cx="35" cy="35" r="27" fill="none" stroke="#fff" stroke-width="2"/><line x1="22" y1="22" x2="48" y2="48" stroke="#fff" stroke-width="2.5"/><circle cx="40" cy="28" r="5" fill="none" stroke="#fff" stroke-width="2.5"/><line x1="37" y1="32" x2="25" y2="45" stroke="#fff" stroke-width="2.5"/><line x1="28" y1="42" x2="31" y2="45" stroke="#fff" stroke-width="2.5"/></svg>
      <span class="system-arrow"></span>
      <span class="system-label">Access Control &amp; Intercom</span>
    </div>
    <div class="system" style="left:655px; top:110px;">
      <svg class="system-icon" viewBox="0 0 70 70"><circle cx="35" cy="35" r="33" fill="#1c2d5a"/><circle cx="35" cy="35" r="27" fill="none" stroke="#fff" stroke-width="2"/><g stroke="#fff" stroke-width="2" fill="none"><rect x="22" y="25" width="26" height="22"/><line x1="22" y1="32" x2="48" y2="32"/><line x1="22" y1="39" x2="48" y2="39"/><line x1="30" y1="25" x2="30" y2="47"/><line x1="39" y1="25" x2="39" y2="47"/></g></svg>
      <span class="system-arrow"></span>
      <span class="system-label">Perimeter Security</span>
    </div>
  </section>

  <section class="benefits">
    <article class="card" style="left:36px; top:51px; width:551px; height:224px;">
      <h2 class="card-title"><strong>Discounted</strong> service rate</h2>
      <p class="card-text">Receive a $20/hour discount on any security related services provided by The Watchpost Depot</p>
    </article>
    <article class="card" style="left:618px; top:51px; width:549px; height:224px;">
      <h2 class="card-title"><strong>Unlimited</strong> Remote Support</h2>
      <p class="card-text">access our highly technical security team with remote web and phone support at no charge to you</p>
    </article>
    <article class="card" style="left:36px; top:310px; width:551px; height:285px;">
      <h2 class="card-title"><strong>Free</strong> Remote Training</h2>
      <p class="card-text">Take advantage of our remote training sessions. Our experienced trainers will guide your existing and new managers through the operation and administration of your security system.</p>
    </article>
    <article class="card" style="left:618px; top:310px; width:549px; height:285px;">
      <h2 class="card-title"><strong>Priority</strong> Support</h2>
      <p class="card-text">As a service plan subscriber you will receive priority support. Your inquiries and requests will be given expedited attention ensuring prompt assistance and minimizing downtime and disruptions to your security system.</p>
    </article>
    <p class="renew renew-title">The plan will automatically renew every year.</p>
    <p class="renew renew-note">All service, training and support is for Monday to Friday during normal working hours.</p>
  </section>

  <footer class="contact">
    <div class="phone">
      <svg width="34" height="34" viewBox="0 0 34 34"><path d="M9 4 L14 10 L11 14 Q14 21 20 23 L24 20 L30 25 L27 30 Q14 31 5 16 Q3 9 9 4 Z" fill="none" stroke="#ea4230" stroke-width="3" stroke-linejoin="round"/></svg>
      <span>1-877-555-0142</span>
    </div>
    <div class="contact-link">
      <svg class="contact-icon" viewBox="0 0 46 46"><circle cx="23" cy="23" r="23" fill="#fff"/><g fill="none" stroke="#1c2d5a" stroke-width="2.4"><circle cx="23" cy="23" r="12"/><ellipse cx="23" cy="23" rx="5" ry="12"/><line x1="11" y1="23" x2="35" y2="23"/></g></svg>
      <span>www.kelvarnguard.com</span>
    </div>
    <div class="contact-link">
      <svg class="contact-icon" viewBox="0 0 46 46"><circle cx="23" cy="23" r="23" fill="#fff"/><rect x="12" y="15" width="22" height="16" rx="2" fill="#1c2d5a"/><path d="M12 16 L23 25 L34 16" fill="none" stroke="#fff" stroke-width="2"/></svg>
      <span>sales@kelvarnguard.com</span>
    </div>
  </footer>

</main>
</body>
</html>
```